Security camera surveillance warning Sign

Security Camera Sign 11" x 11" Red, Yellow and Black (White Background)
I would like a line drawing of camera image attached.
Wording: All Suspicious or Criminal Activity Will Be Reported!
WARNING
24 HOUR SURVEILLANCE

Industry/Entity Type

Security

Colors
ec1f27
000000
ffc214

Requirements
Nice to have
• I uploaded a sign and would like the new design look something like that

```html
<!DOCTYPE html>
<html lang="en">
<head>
<meta charset="utf-8">
<title>Security Notice – 24 Hours Surveillance</title>
<link rel="stylesheet" href="https://fonts.googleapis.com/css2?family=Open+Sans:wght@600;700;800&display=swap">
<style>
  :root {
    --sign-red: #ec1f27;
    --sign-yellow: #fff200;
    --sign-black: #1a1a1a;
    --sign-white: #ffffff;
    --camera-dark: #1f1f1f;
    --camera-mid: #4a4a4a;
    --camera-light: #bdbdbd;
  }
  html, body {
    margin: 0;
    padding: 0;
    width: 1200px;
    height: 1200px;
    overflow: hidden;
    background: var(--sign-white);
  }
  .sign {
    position: relative;
    width: 1200px;
    height: 1200px;
    font-family: "Open Sans", Arial, sans-serif;
  }
  .sign-frame {
    position: absolute;
    left: 42px; top: 42px;
    width: 1116px; height: 1116px;
    box-sizing: border-box;
    background: var(--sign-red);
    border: 5px solid var(--sign-black);
    border-radius: 30px;
  }
  .warning-banner {
    position: absolute;
    left: 102px; top: 78px;
    width: 996px; height: 188px;
    box-sizing: border-box;
    background: var(--sign-yellow);
    border: 4px solid var(--sign-black);
    border-radius: 24px;
    display: flex;
    align-items: center;
    justify-content: center;
  }
  .warning-title {
    margin: 0 -5px 0 0;
    font-weight: 800;
    font-size: 172px;
    line-height: 1;
    letter-spacing: 5px;
    color: var(--sign-black);
    transform: translateY(-4px);
  }
  .notice-panel {
    position: absolute;
    left: 50px; top: 294px;
    width: 1100px; height: 720px;
    box-sizing: border-box;
    background: var(--sign-white);
    border: 4px solid var(--sign-black);
    border-radius: 14px;
  }
  .hours-badge {
    position: absolute;
    left: 84px; top: 394px;
    width: 298px; height: 297px;
    box-sizing: border-box;
    border: 5px solid var(--sign-red);
    border-radius: 12px;
    color: var(--sign-red);
    font-weight: 700;
  }
  .hours-badge span {
    position: absolute;
    left: 0; right: 0;
    text-align: center;
    line-height: 1;
    white-space: nowrap;
  }
  .hours-number {
    top: -23px;
    font-size: 218px;
    letter-spacing: -2px;
  }
  .hours-label {
    top: 173px;
    font-size: 72px;
  }
  .hours-caption {
    top: 243px;
    font-size: 35px;
    letter-spacing: -0.5px;
  }
  .report-statement {
    position: absolute;
    left: 104px; top: 729px;
    margin: 0;
    font-weight: 700;
    font-size: 56px;
    line-height: 78px;
    letter-spacing: -0.5px;
    color: var(--sign-black);
    white-space: nowrap;
  }
  .camera-illustration {
    position: absolute;
    left: 426px; top: 336px;
    width: 684px; height: 612px;
    background: linear-gradient(160deg, var(--camera-dark) 0%, var(--camera-mid) 60%, var(--camera-light) 100%);
    clip-path: polygon(0 0, 100% 0, 100% 100%, 47% 100%, 47% 60%, 0 60%);
  }
  .security-footer {
    position: absolute;
    left: 42px; top: 1014px;
    width: 1116px; height: 136px;
    display: flex;
    align-items: center;
    justify-content: center;
  }
  .security-title {
    margin: 0;
    font-weight: 600;
    font-size: 106px;
    line-height: 1;
    color: var(--sign-white);
    transform: translateY(-4px);
  }
</style>
</head>
<body>
  <main class="sign">
    <div class="sign-frame"></div>

    <header class="warning-banner">
      <h1 class="warning-title">WARNING</h1>
    </header>

    <section class="notice-panel"></section>

    <div class="hours-badge">
      <span class="hours-number">24</span>
      <span class="hours-label">HOURS</span>
      <span class="hours-caption">SURVEILLANCE</span>
    </div>

    <div class="camera-illustration" role="img" aria-label="Black and white line illustration of a wall-mounted security camera"></div>

    <p class="report-statement">ALL SUSPICIOUS OR<br>CRIMINAL ACTIVITY<br>WILL BE REPORTED!</p>

    <footer class="security-footer">
      <h2 class="security-title">SECURITY NOTICE</h2>
    </footer>
  </main>
</body>
</html>
```